Security Officer Training Certifications POSTCARD

We need Post Card Design
-Front and Back
-In Compliance with MERLO PRESS for upload!
-For Oversized and Jumbo Size Cards (merlo presses)
Our Company:
www.brandelhollowacademy.org (FOR IDEAS)
We provide Corporate Security Officer/Criminal Justice/Police Tactics Training for Private Companies that have a security department and officers.
We provide:
Handcuffing certifications
Pepper Spray
Compliance Training
Instructor Training
California Guard Card
Our Card to display powerful image for a Security Officer Department
Traits in Pic and Deigns
VALUE
COMPETITIVE EDGE
PROFESSIONAL GROWTH
QUALITY
PROFICIENT/EFFECTIVE SECURITY OFFICERS
TACTICAL OFFICERS
PROFESSIONALISM
EXPERTS
INDUSTRY LEADERS
READINESS
FRONT DESIGN TO BE VERY CATCH AND ATTRACTIVE!
-Please put the images of lawn enforcement, security guards, public safety department in the FRONT
BACK OF THE CARD DESIGN
-Please put our Services/Menu, CREATIVE and CATCHY, in columns and with vivid colors.

```html
<!DOCTYPE html>
<html lang="en">
<head>
<meta charset="UTF-8">
<title>Security Guard Training Postcard</title>
<link href="https://fonts.googleapis.com/css2?family=Oswald:wght@500;600&family=Lato:wght@400;700&display=swap" rel="stylesheet">
<style>
  :root {
    --page-bg: #e9eaec;
    --card-white: #ffffff;
    --blue-bright: #2a86cf;
    --blue-deep: #1c4fa3;
    --blue-mid: #2f6fc2;
    --blue-pale: #9fd8ea;
    --text-gray: #5a5a5a;
    --line-dark: #1a1a1a;
    --stamp-dark: #2b2b2b;
  }
  html, body {
    margin: 0;
    padding: 0;
    width: 1200px;
    height: 800px;
    overflow: hidden;
    background: var(--page-bg);
  }
  .canvas {
    position: relative;
    width: 1200px;
    height: 800px;
  }
  .postcard {
    position: absolute;
    top: 213px;
    width: 580px;
    height: 374px;
    background: var(--card-white);
    overflow: hidden;
    box-shadow: 0 4px 14px rgba(0,0,0,0.18);
  }
  .postcard--front { left: 10px; }
  .postcard--back { left: 610px; }

  .front-art {
    position: absolute;
    inset: 0;
  }
  .headline {
    position: absolute;
    left: 24px;
    top: 16px;
    margin: 0;
    font-family: "Oswald", sans-serif;
    font-weight: 600;
    color: var(--blue-bright);
    line-height: 1;
    text-transform: uppercase;
  }
  .headline__main {
    display: block;
    font-size: 72px;
  }
  .headline__sub {
    display: block;
    font-size: 36px;
    margin-top: 4px;
  }
  .band-text {
    position: absolute;
    left: 28px;
    top: 176px;
    margin: 0;
    font-family: "Oswald", sans-serif;
    font-weight: 500;
    font-size: 30px;
    line-height: 1.08;
    color: var(--card-white);
    text-transform: uppercase;
  }
  .front-blurb {
    position: absolute;
    left: 22px;
    top: 302px;
    width: 330px;
    margin: 0;
    font-family: "Lato", sans-serif;
    font-weight: 700;
    font-size: 12.5px;
    line-height: 1.3;
    color: var(--blue-mid);
  }

  .services {
    position: absolute;
    left: 30px;
    top: 32px;
    font-family: "Lato", sans-serif;
    font-size: 15px;
    line-height: 1.3;
    color: var(--text-gray);
  }
  .services__title { margin: 0; font-weight: 400; font-size: 15px; }
  .services__list { list-style: none; margin: 0; padding: 0; }

  .stamp-box {
    position: absolute;
    right: 28px;
    top: 24px;
    width: 68px;
    height: 72px;
    background: var(--stamp-dark);
  }
  .badges {
    position: absolute;
    left: 270px;
    top: 50px;
    width: 220px;
    height: 160px;
  }
  .address-lines {
    position: absolute;
    left: 300px;
    top: 230px;
    width: 250px;
  }
  .address-lines span {
    display: block;
    height: 0;
    border-top: 2px solid var(--line-dark);
    margin-bottom: 42px;
  }
</style>
</head>
<body>
<main class="canvas">

  <section class="postcard postcard--front" aria-label="Postcard front">
    <svg class="front-art" width="580" height="374" viewBox="0 0 580 374">
      <defs>
        <linearGradient id="bandFill" x1="0" y1="0" x2="1" y2="0">
          <stop offset="0" stop-color="#2f7fd0"/>
          <stop offset="1" stop-color="#1c4fa3"/>
        </linearGradient>
        <linearGradient id="photoFill" x1="0" y1="0" x2="0" y2="1">
          <stop offset="0" stop-color="#bcd6ec"/>
          <stop offset="0.35" stop-color="#8fa4b8"/>
          <stop offset="0.55" stop-color="#2c2f36"/>
          <stop offset="1" stop-color="#23252b"/>
        </linearGradient>
      </defs>
      <rect class="name-band" x="0" y="170" width="330" height="122" fill="url(#bandFill)"/>
      <path class="hero-photo" role="img" aria-label="Photo of a uniformed security officer seen from behind, radio and duty belt, city towers in the background"
            d="M 358 0 L 580 0 L 580 374 L 498 374 C 358 280, 328 150, 358 0 Z" fill="url(#photoFill)"/>
      <path class="swoosh swoosh--deep" d="M 330 0 C 300 150, 330 280, 470 374" fill="none" stroke="#1c4fa3" stroke-width="26"/>
      <path class="swoosh swoosh--bright" d="M 344 0 C 314 150, 344 280, 484 374" fill="none" stroke="#2a86cf" stroke-width="8"/>
      <path class="swoosh swoosh--pale" d="M 353 0 C 323 150, 353 280, 493 374" fill="none" stroke="#9fd8ea" stroke-width="9"/>
    </svg>
    <h1 class="headline">
      <span class="headline__main">Security</span>
      <span class="headline__sub">Guard Training</span>
    </h1>
    <p class="band-text">In Los Angeles<br>California Guard<br>Card Specialists</p>
    <p class="front-blurb">We provide Corporate Security Officer/ Criminal Justice/Police Tactics Training for Private Companies that have a security department and officers.</p>
  </section>

  <section class="postcard postcard--back" aria-label="Postcard back">
    <div class="services">
      <h2 class="services__title">We provide:</h2>
      <ul class="services__list">
        <li>Handcuffing certifications</li>
        <li>Pepper Spray</li>
        <li>Compliance Training</li>
        <li>Instructor Training</li>
        <li>California Guard Card</li>
      </ul>
    </div>
    <div class="stamp-box" aria-hidden="true"></div>
    <svg class="badges" width="220" height="160" viewBox="0 0 220 160" role="img" aria-label="Certification badges">
      <ellipse cx="45" cy="60" rx="44" ry="56" fill="#c9c9cc"/>
      <path d="M 100 10 L 160 10 L 160 50 C 160 72, 130 84, 130 84 C 130 84, 100 72, 100 50 Z" fill="#b3262b"/>
      <path d="M 102 100 L 150 100 L 150 128 C 150 146, 126 156, 126 156 C 126 156, 102 146, 102 128 Z" fill="#a7a9ad"/>
      <rect x="165" y="82" width="55" height="72" fill="#141414"/>
    </svg>
    <div class="address-lines" aria-hidden="true">
      <span></span><span></span><span></span>
    </div>
  </section>

</main>
</body>
</html>
```